Bodywork Quietude Business Card Design

I want to create a very elegant and sophisticated two sided business card for my massage practice (www.bodyworkquietude.net). I have attached the logo and a PDF with some ideas down for the back of the card but I am open to suggestions. I will want to tie in a post card and flyer to the card later.
Similar colors to website would be great.
Target Market(s)
High end clientele, people looking for a sophisticated spa experience.
Industry/Entity Type
Massage
Contact Information for Business Card
Bodywork Quietude
7318 Larkspur Ave S, Suite 305
Seattle, WA 98103
(206) 555-0147
www.bodyworkquietude.net
Look and feel

```html
<!DOCTYPE html>
<html lang="en">
<head>
<meta charset="utf-8">
<title>Bodywork Quietude – Business Card</title>
<link rel="stylesheet" href="https://fonts.googleapis.com/css2?family=Arimo:wght@400;700&display=swap">
<style>
  :root {
    --backdrop: #5e4a36;
    --card-cream: #eeebe5;
    --card-cream-edge: #e2ddd5;
    --teal-deep: #173848;
    --teal: #1f4a5c;
    --teal-light: #2c5f73;
    --ink: #1c3f50;
    --light-text: #f1eee8;
  }
  * { margin: 0; padding: 0; box-sizing: border-box; }
  html, body { width: 1200px; height: 1023px; overflow: hidden; }
  body {
    position: relative;
    background: var(--backdrop);
    font-family: "Arimo", Arial, sans-serif;
  }
  .card {
    position: absolute;
    left: 258px;
    width: 682px;
    height: 390px;
    box-shadow: 0 4px 14px rgba(0, 0, 0, 0.35);
    text-align: center;
  }
  .card-front {
    top: 88px;
    background: radial-gradient(ellipse at 50% 40%, var(--card-cream) 60%, var(--card-cream-edge) 100%);
    color: var(--ink);
  }
  .brand-band {
    position: absolute;
    top: 104px; left: 0; width: 100%; height: 56px;
    background: var(--teal);
  }
  .brand-name {
    font-family: "Arimo", Arial, sans-serif;
    font-weight: 400;
    font-size: 28px;
    line-height: 56px;
    letter-spacing: 0.5px;
    color: var(--light-text);
  }
  .contact-address {
    position: absolute;
    top: 252px; left: 0; width: 100%;
    font-size: 18.5px;
    line-height: 22px;
  }
  .contact-rule {
    position: absolute;
    top: 298px; left: 109px; width: 459px;
    border-top: 1.5px solid var(--ink);
  }
  .contact-reach {
    position: absolute;
    top: 306px; left: 0; width: 100%;
    font-size: 18.5px;
    line-height: 22px;
  }
  .card-back {
    top: 528px;
    background: radial-gradient(ellipse at 45% 30%, var(--teal-light) 0%, var(--teal) 45%, var(--teal-deep) 100%);
    color: var(--light-text);
  }
  .specialties {
    position: absolute;
    top: 41px; left: 0; width: 100%;
    list-style: none;
    font-weight: 700;
    font-size: 21px;
    line-height: 24.5px;
    text-transform: uppercase;
  }
  .promise-band {
    position: absolute;
    top: 224px; left: 0; width: 100%; height: 63px;
    background: var(--card-cream);
    color: var(--ink);
    font-weight: 700;
    font-size: 18.5px;
    line-height: 25px;
    padding-top: 7px;
  }
</style>
</head>
<body>
  <section class="card card-front">
    <div class="brand-band">
      <h1 class="brand-name">Bodywork Quietude</h1>
    </div>
    <p class="contact-address">7318 Larkspur Ave S, Suite 305<br>Seattle, WA 98103</p>
    <div class="contact-rule"></div>
    <p class="contact-reach">(206) 555-0147<br>www.bodyworkquietude.net</p>
  </section>

  <section class="card card-back">
    <ul class="specialties">
      <li>Our Specialties :</li>
      <li>Deep Lomi Ultra Relaxation Massage</li>
      <li>Nurturing Touch Massage</li>
      <li>Hot Yoga Massage</li>
    </ul>
    <p class="promise-band">Experience the Most Relaxing and Invitingly Deep<br>Massage of Your Life.....</p>
  </section>
</body>
</html>
```